" distribuir internet através de fibra óptica em condomínios de alto e médio padrão, também podendo atender empresas e domicílios fora de condominios "

```html
<!DOCTYPE html>
<html lang="pt-BR">
<head>
<meta charset="utf-8">
<title>Assinatura de e-mail — Fibralux</title>
<link rel="stylesheet" href="https://fonts.googleapis.com/css2?family=Arimo:wght@400;700&display=swap">
<style>
  :root {
    --page-bg: #e6e8ea;
    --band-teal: #2f7f93;
    --band-teal-dark: #1f5a6a;
    --card-light: #ffffff;
    --card-shade: #e4e6e8;
    --text-dark: #2a2d30;
    --text-mid: #55595d;
    --icon-bg: #34383c;
    --brand: #2a8aa0;
  }
  html, body {
    margin: 0;
    padding: 0;
    width: 1200px;
    height: 1200px;
    overflow: hidden;
    background: var(--page-bg);
    font-family: "Arimo", Arial, sans-serif;
  }
  .signature {
    position: absolute;
    left: 85px;
    top: 480px;
    width: 1030px;
    height: 240px;
    background: linear-gradient(180deg, var(--card-light) 0%, #f4f5f6 55%, var(--card-shade) 100%);
    box-shadow: 0 6px 18px rgba(0,0,0,0.18);
  }
  .band {
    position: absolute;
    left: 0;
    width: 100%;
    height: 16px;
    background: linear-gradient(180deg, var(--band-teal) 0%, var(--band-teal-dark) 100%);
  }
  .band--top { top: 0; }
  .band--bottom { bottom: 0; }
  .brand {
    position: absolute;
    left: 58px;
    top: 92px;
    display: flex;
    align-items: center;
    gap: 14px;
  }
  .brand__dot {
    width: 18px;
    height: 18px;
    border-radius: 50%;
    background: var(--brand);
  }
  .brand__name {
    font-size: 46px;
    font-weight: 700;
    letter-spacing: 2px;
    color: var(--brand);
  }
  .divider {
    position: absolute;
    left: 340px;
    top: 50px;
    height: 140px;
    border-left: 2px dotted #c3c7ca;
  }
  .person {
    position: absolute;
    left: 452px;
    top: 40px;
  }
  .person__name {
    margin: 0;
    font-size: 27px;
    font-weight: 400;
    color: var(--text-dark);
    letter-spacing: 0.5px;
  }
  .person__role {
    margin: 4px 0 0;
    font-size: 15px;
    color: var(--text-mid);
  }
  .contact {
    position: absolute;
    display: flex;
    align-items: center;
    gap: 14px;
    font-size: 15px;
    color: var(--text-dark);
  }
  .contact--address { left: 458px; top: 128px; }
  .contact--phone   { left: 458px; top: 170px; }
  .contact--email   { left: 722px; top: 170px; }
  .contact__icon {
    width: 22px;
    height: 22px;
    flex: none;
  }
</style>
</head>
<body>
  <div class="signature">
    <div class="band band--top"></div>

    <div class="brand">
      <span class="brand__dot"></span>
      <span class="brand__name">FIBRALUX</span>
    </div>

    <div class="divider"></div>

    <div class="person">
      <p class="person__name">NOME SOBRONOME</p>
      <p class="person__role">CARGO/FUNÇÃO</p>
    </div>

    <div class="contact contact--address">
      <svg class="contact__icon" viewBox="0 0 22 22" aria-hidden="true">
        <rect width="22" height="22" rx="2" fill="#34383c"/>
        <path d="M11 4.5a4.5 4.5 0 0 0-4.5 4.5c0 3.3 4.5 8.5 4.5 8.5s4.5-5.2 4.5-8.5A4.5 4.5 0 0 0 11 4.5zm0 6.3a1.8 1.8 0 1 1 0-3.6 1.8 1.8 0 0 1 0 3.6z" fill="#ffffff"/>
      </svg>
      <span>Rua do Projeto, 00 - cidade - Estado - SP - 00000-000</span>
    </div>

    <div class="contact contact--phone">
      <svg class="contact__icon" viewBox="0 0 22 22" aria-hidden="true">
        <rect width="22" height="22" rx="2" fill="#34383c"/>
        <path d="M7.2 5h2.2l1 3-1.4 1.1a7.5 7.5 0 0 0 3.9 3.9L14 11.6l3 1v2.2c0 .7-.5 1.2-1.2 1.2A10.8 10.8 0 0 1 6 6.2C6 5.5 6.5 5 7.2 5z" fill="#ffffff"/>
      </svg>
      <span>(11) 0000-0000</span>
    </div>

    <div class="contact contact--email">
      <svg class="contact__icon" viewBox="0 0 22 22" aria-hidden="true">
        <rect width="22" height="22" rx="2" fill="#34383c"/>
        <rect x="4.5" y="6.5" width="13" height="9" rx="1" fill="#ffffff"/>
        <path d="M4.8 7l6.2 4.6L17.2 7" fill="none" stroke="#34383c" stroke-width="1.3"/>
      </svg>
      <span>contato@empresa.com.br</span>
    </div>

    <div class="band band--bottom"></div>
  </div>
</body>
</html>
```